Poster to advertise new mind coaching clinic

Create a single sided A4 colour poster using the text provided. Suggested image provided. You may want to suggest an alternative however images need to appeal to both male and female sports people.

Text:
One-to-one mind coaching
For recreational and competitive sports people
Learn the mental tools and techniques used by the top sports people to fulfil your potential

 Create well-formed and achievable goals
 Overcome limiting beliefs
 Accelerate mastery through modelling your heroes
 Learn how to use mental rehearsal to increase your chances of success
 Smash through belief ceilings
 Get into the zone to bring your ‘A-Game’ more often
Thursdays in central Twyford
5-8pm
For more information contact:
thebluekitecoaching@postmere.com
Tel: 07481 265314
www.the-blue-kite.co.uk

Target Market(s)

sports people

Industry/Entity Type

Clinic

Requirements
Must have
• All the content provided. Contact details.

```html
<!DOCTYPE html>
<html lang="en">
<head>
<meta charset="utf-8">
<title>One-to-one mind coaching – The Blue Kite</title>
<link rel="stylesheet" href="https://fonts.googleapis.com/css2?family=Anton&family=Open+Sans:ital,wght@0,400;0,600;0,700;1,400&display=swap">
<style>
  :root {
    --cyan: #5dd5e6;
    --cyan-pale: #d4f1f6;
    --blue: #1c5be0;
    --blue-deep: #0f3fb4;
    --ink: #141414;
    --white: #ffffff;
  }
  * { box-sizing: border-box; margin: 0; padding: 0; }
  html, body { width: 856px; height: 1200px; overflow: hidden; background: var(--white); }
  .poster {
    position: relative; width: 856px; height: 1200px; overflow: hidden;
    background: var(--white); font-family: "Open Sans", Arial, sans-serif; color: var(--ink);
  }
  .hero-backdrop {
    position: absolute; left: 0; top: 0; width: 856px; height: 605px;
    background: linear-gradient(160deg, #eaf8fb 0%, var(--cyan-pale) 45%, #c2e9f1 100%);
  }
  .hero-circle {
    position: absolute; left: 168px; top: 22px; width: 540px; height: 540px; border-radius: 50%;
    background: radial-gradient(circle at 50% 45%, #7fd0f0 0%, #3fa6e0 60%, #2b86cc 100%);
  }
  .hero-athlete {
    position: absolute; left: 90px; top: 0; width: 700px; height: 600px;
    background: radial-gradient(ellipse at 52% 40%, rgba(120,70,50,0.55) 0%, rgba(120,70,50,0.25) 30%, rgba(120,70,50,0) 60%);
  }
  .headline {
    position: absolute; left: 0; top: 318px; width: 856px; text-align: center;
    font-family: "Anton", Impact, sans-serif; font-weight: 400; font-size: 118px; line-height: 112px;
    color: var(--white); -webkit-text-stroke: 4px var(--ink); paint-order: stroke fill;
    letter-spacing: -1px;
  }
  .audience {
    position: absolute; left: 72px; top: 564px; width: 696px; height: 50px; border-radius: 25px;
    background: var(--cyan); color: var(--white); font-weight: 600; font-size: 28px;
    line-height: 50px; text-align: center;
  }
  .intro {
    position: absolute; left: 0; top: 626px; width: 856px; text-align: center;
    font-weight: 700; font-size: 22px; line-height: 35px;
  }
  .benefits { position: absolute; left: 74px; top: 700px; list-style: none; }
  .benefits li {
    position: relative; padding-left: 32px; font-size: 19.5px; line-height: 38px;
  }
  .benefits li::before {
    content: ""; position: absolute; left: 4px; top: 12px; width: 14px; height: 14px;
    border-radius: 50%; background: var(--ink); box-shadow: 3px 0 0 var(--cyan);
  }
  .session-badge {
    position: absolute; left: 628px; top: 690px; width: 188px; height: 188px; border-radius: 50%;
    background: var(--blue); border: 7px solid var(--white);
    box-shadow: 0 4px 12px rgba(0,0,0,0.3);
    display: flex; align-items: center; justify-content: center; text-align: center;
    color: var(--white); font-weight: 700; font-size: 21px; line-height: 30px;
  }
  .swoosh { position: absolute; left: 0; top: 900px; width: 856px; height: 300px; }
  .contact-label {
    position: absolute; left: 166px; top: 940px; font-style: italic; font-size: 20px;
  }
  .contact-list { position: absolute; left: 460px; top: 930px; list-style: none; }
  .contact-list li { display: flex; align-items: center; height: 46px; margin-bottom: 12px; }
  .contact-icon {
    width: 38px; height: 44px; border-radius: 10px; background: var(--blue);
    display: flex; align-items: center; justify-content: center; margin-right: 10px; flex: none;
  }
  .contact-phone { font-size: 30px; }
  .contact-web { font-size: 26px; }
  .contact-mail { font-size: 19px; }
  .brand {
    position: absolute; left: 56px; top: 985px; display: flex; align-items: center;
  }
  .brand-dot { width: 46px; height: 46px; border-radius: 50%; background: var(--cyan); margin-right: 14px; }
  .brand-name { font-weight: 700; font-size: 40px; color: var(--ink); }
  .baton {
    position: absolute; left: 120px; top: 1095px; width: 240px; height: 44px; border-radius: 8px;
    background: linear-gradient(180deg, #f4f4f4 0%, #bfc4c8 50%, #8e959b 100%);
    transform: rotate(9deg);
  }
  .social { position: absolute; left: 686px; top: 1124px; display: flex; gap: 8px; }
  .social span { width: 38px; height: 38px; border-radius: 50%; background: var(--blue); }
</style>
</head>
<body>
<main class="poster">
  <div class="hero-backdrop" role="img" aria-label="Faded photo of an athletics track in pale blue tones"></div>
  <div class="hero-circle"></div>
  <div class="hero-athlete" role="img" aria-label="Photo of a sprinter crossing the finish line with arms raised, holding a relay baton"></div>

  <h1 class="headline">One-to-one<br>mind coaching</h1>
  <p class="audience">For recreational and competitive sports people</p>

  <p class="intro">Learn the mental tools and techniques used<br>by the top sports people to fulfil your potential</p>

  <ul class="benefits">
    <li>Create well-formed and achievable goals</li>
    <li>Overcome limiting beliefs</li>
    <li>Accelerate mastery through modelling your heroes</li>
    <li>Smash through belief ceilings</li>
    <li>Get into the zone to bring your 'A-Game' more often</li>
    <li>Learn how to use mental rehearsal to increase your chances of success</li>
  </ul>

  <div class="session-badge">5-8PM<br>THURSDAYS<br>IN CENTRAL<br>TWYFORD</div>

  <svg class="swoosh" viewBox="0 0 856 300" aria-hidden="true">
    <path d="M0 230 C 250 190 560 120 856 40 L856 300 L0 300 Z" fill="var(--cyan)"/>
    <path d="M0 262 C 260 222 560 160 856 92 L856 128 C 560 200 270 256 0 290 Z" fill="var(--white)"/>
  </svg>

  <p class="contact-label">For more information contact:</p>
  <ul class="contact-list">
    <li>
      <span class="contact-icon">
        <svg width="18" height="30" viewBox="0 0 18 30"><rect x="1" y="1" width="16" height="28" rx="3" fill="none" stroke="#fff" stroke-width="2"/><circle cx="9" cy="24" r="1.8" fill="#fff"/></svg>
      </span>
      <span class="contact-phone">07481 265314</span>
    </li>
    <li>
      <span class="contact-icon">
        <svg width="26" height="24" viewBox="0 0 26 24"><rect x="1" y="1" width="24" height="16" rx="2" fill="none" stroke="#fff" stroke-width="2"/><rect x="9" y="19" width="8" height="3" fill="#fff"/></svg>
      </span>
      <span class="contact-web">www.the-blue-kite.co.uk</span>
    </li>
    <li>
      <span class="contact-icon">
        <svg width="26" height="18" viewBox="0 0 26 18"><rect x="1" y="1" width="24" height="16" rx="2" fill="none" stroke="#fff" stroke-width="2"/><path d="M2 2 L13 10 L24 2" fill="none" stroke="#fff" stroke-width="2"/></svg>
      </span>
      <span class="contact-mail">thebluekitecoaching@postmere.com</span>
    </li>
  </ul>

  <div class="brand">
    <span class="brand-dot"></span>
    <span class="brand-name">The Blue Kite</span>
  </div>

  <div class="baton" role="img" aria-label="Photo of a silver relay baton"></div>

  <div class="social" aria-hidden="true"><span></span><span></span><span></span></div>
</main>
</body>
</html>
```